indoor tennis and sports center( club)

we need a logo for a new business venture, it will be for business cards and for presentations.
presentations for potential investors and authorities.
the design needs to communicate the sport and a community of tennis players
the center includes a tennis academy, and sports club with training sessions for all ages

Project Deadline Extended
Reason: so that I can get some more feedback on my side as to te design we want

Target Market(s)

potential investors or partners

Industry/Entity Type

Business

Contact Information for Business Card

i need the name of the club
names of the partners
slogan" changing lives through tennis" on the front
the clubs three main goals are ports education , academy and a community club

Colors
3176b5
33b8a4
fbee3d
0dac94
acd036

Requirements
Must have
• a strong logo
• names of the partners
• web site and email address
• tel number
Nice to have
• a connection between the different aspects of the club

```html
<!DOCTYPE html>
<html lang="en">
<head>
<meta charset="utf-8">
<title>Baseline Indoor Tennis and Sports Club – Business Card</title>
<link rel="stylesheet" href="https://fonts.googleapis.com/css2?family=Jost:wght@400;500&display=swap">
<style>
  :root {
    --blue: #3176b5;
    --teal: #33b8a4;
    --yellow: #fbee3d;
    --lime: #acd036;
    --backdrop: #ebe7e0;
  }
  * { margin: 0; padding: 0; box-sizing: border-box; }
  html, body {
    width: 1200px;
    height: 1200px;
    overflow: hidden;
    background: var(--backdrop);
    font-family: "Jost", "Century Gothic", sans-serif;
  }
  .card {
    position: absolute;
    left: 220px;
    width: 760px;
    height: 456px;
    overflow: hidden;
    background: var(--teal);
  }
  .card--front { top: 80px; }
  .card--back { top: 664px; }
  .card__bg {
    position: absolute;
    inset: 0;
    width: 100%;
    height: 100%;
  }
  .card__bg .band-blue { fill: var(--blue); }
  .card__bg .band-lime { fill: var(--lime); }

  .club-mark {
    position: absolute;
    display: flex;
    align-items: center;
    gap: 14px;
    color: var(--yellow);
    font-weight: 500;
    white-space: nowrap;
  }
  .club-mark__dot {
    border-radius: 50%;
    background: var(--yellow);
    flex: none;
  }
  .card--front .club-mark {
    left: 50%;
    top: 200px;
    transform: translateX(-50%);
    font-size: 34px;
  }
  .card--front .club-mark__dot { width: 56px; height: 56px; }

  .tagline {
    position: absolute;
    left: 0;
    right: 0;
    top: 410px;
    text-align: center;
    color: var(--yellow);
    font-size: 20px;
    font-weight: 400;
  }

  .contact {
    position: absolute;
    left: 24px;
    top: 26px;
    color: var(--yellow);
  }
  .contact__club {
    font-size: 30px;
    font-weight: 400;
    letter-spacing: 0.3px;
    line-height: 1.2;
  }
  .contact__partners {
    margin-top: 12px;
    margin-left: 3px;
    font-size: 20px;
  }
  .contact__list {
    list-style: none;
    margin-top: 24px;
    margin-left: 3px;
    font-size: 16.5px;
    line-height: 28px;
  }
  .card--back .club-mark {
    right: 40px;
    top: 250px;
    font-size: 36px;
  }
  .card--back .club-mark__dot { width: 70px; height: 70px; }
</style>
</head>
<body>

  <section class="card card--front">
    <svg class="card__bg" viewBox="0 0 760 456" preserveAspectRatio="none" aria-hidden="true">
      <polygon class="band-blue" points="0,0 676,0 0,318"/>
      <polygon class="band-lime" points="0,318 50,298 236,456 0,456"/>
    </svg>
    <div class="club-mark">
      <span class="club-mark__dot"></span>
      <span class="club-mark__name">Baseline Tennis Club</span>
    </div>
    <p class="tagline">“Changing lives through Tennis”</p>
  </section>

  <section class="card card--back">
    <svg class="card__bg" viewBox="0 0 760 456" preserveAspectRatio="none" aria-hidden="true">
      <polygon class="band-blue" points="0,0 676,0 0,318"/>
      <polygon class="band-lime" points="0,318 50,298 236,456 0,456"/>
    </svg>
    <div class="contact">
      <h1 class="contact__club">Baseline Indoor Tennis and Sports Club</h1>
      <p class="contact__partners">Partners and Investors here.</p>
      <ul class="contact__list">
        <li>www.baselineindoortennisclub.com</li>
        <li>hello@baselinetennisclub.com</li>
        <li>XXX - XXX - XXXX</li>
      </ul>
    </div>
    <div class="club-mark">
      <span class="club-mark__dot"></span>
      <span class="club-mark__name">Baseline</span>
    </div>
  </section>

</body>
</html>
```